We need a business card design for a new company based in
Perth, Western Australia called Oveko Tiling Services. We specialize in laying Wall and Floor Tiles and Stone. We expertise in all small to large format tiles and do good quality work. Sincerity and Convition is what seperates us from others.

```html
<!DOCTYPE html>
<html lang="en">
<head>
<meta charset="utf-8">
<title>Oveko Tiling Services – Business Cards</title>
<link rel="stylesheet" href="https://fonts.googleapis.com/css2?family=Oxygen:wght@400&display=swap">
<style>
  :root {
    --stage: #c0c0c0;
    --paper: #ffffff;
    --ink: #151515;
    --ink-soft: #5a5a5a;
    --night: #121110;
    --night-tile: #222221;
    --night-text: #d4d4d4;
    --night-soft: #8a8a8a;
    --tile-light: #dcdcdc;
    --tile-light-edge: #e8e8e8;
  }
  * { margin: 0; padding: 0; box-sizing: border-box; }
  html, body { width: 1200px; height: 1000px; overflow: hidden; }
  body {
    background: var(--stage);
    position: relative;
    font-family: "Oxygen", Arial, sans-serif;
  }
  .card {
    position: absolute;
    width: 452px;
    height: 264px;
    background: var(--paper);
    color: var(--ink);
    overflow: hidden;
  }
  .card--dark { background: var(--night); color: var(--night-text); }

  .tile-strip {
    position: absolute;
    left: 0; top: 0;
    width: 99px; height: 100%;
    background: linear-gradient(90deg, var(--tile-light) 0%, var(--tile-light) 70%, var(--tile-light-edge) 100%);
  }
  .card--dark .tile-strip {
    background: linear-gradient(90deg, var(--night-tile) 0%, var(--night-tile) 70%, #1a1918 100%);
  }

  /* Front */
  .front-name {
    position: absolute;
    left: 146px; top: 96px;
    width: 168px;
    text-align: center;
    text-transform: uppercase;
    font-weight: 400;
    color: var(--ink);
  }
  .card--dark .front-name { color: var(--night-text); }
  .front-name .word { display: block; font-size: 44px; letter-spacing: 2px; line-height: 50px; }
  .front-name .sub { display: block; font-size: 12px; letter-spacing: 2.6px; line-height: 18px; }
  .web {
    position: absolute;
    left: 0; right: 0; bottom: 8px;
    padding-left: 24px;
    text-align: center;
    font-size: 10px;
    letter-spacing: 2.4px;
    color: var(--ink);
  }
  .card--dark .web { color: #3a3a3a; }

  /* Back */
  .back-name {
    position: absolute;
    right: 24px; top: 16px;
    text-align: center;
    text-transform: uppercase;
    color: var(--ink);
  }
  .card--dark .back-name { color: var(--night-text); }
  .back-name .word { display: block; font-size: 26px; letter-spacing: 1px; line-height: 30px; }
  .back-name .sub { display: block; font-size: 7.5px; letter-spacing: 1.2px; line-height: 10px; }

  .person { position: absolute; right: 26px; top: 83px; text-align: right; font-size: 11px; line-height: 14px; }
  .person .title { color: var(--ink-soft); }
  .card--dark .person .title { color: var(--night-soft); }

  .contacts { position: absolute; right: 26px; top: 130px; list-style: none; font-size: 10px; }
  .contacts li { display: flex; justify-content: flex-end; align-items: center; height: 18.5px; color: var(--ink-soft); }
  .card--dark .contacts li { color: var(--night-soft); }
  .contacts svg { width: 11px; height: 11px; margin-left: 13px; fill: var(--ink); }
  .card--dark .contacts svg { fill: var(--night-text); }

  .address { position: absolute; right: 26px; top: 225px; text-align: right; font-size: 10px; line-height: 12px; color: var(--ink); }
  .card--dark .address { color: var(--night-soft); }
</style>
</head>
<body>

<!-- Row 1 -->
<section class="card card--front" style="left:120px;top:33px;">
  <div class="tile-strip" role="img" aria-label="Light grey diagonal floor-tile pattern"></div>
  <div class="front-name"><span class="word">Oveko</span><span class="sub">Tiling Services</span></div>
  <p class="web">www.ovekotiling.com</p>
</section>

<section class="card card--back card--dark" style="left:602px;top:35px;">
  <div class="tile-strip" role="img" aria-label="Dark diagonal floor-tile pattern"></div>
  <div class="back-name"><span class="word">Oveko</span><span class="sub">Tiling Services</span></div>
  <div class="person"><p class="name">Daniel Harlow</p><p class="title">President</p></div>
  <ul class="contacts">
    <li>+ 254 5810 33470<svg viewBox="0 0 12 12"><rect x="0" y="0" width="12" height="12" rx="1.5"/><path d="M4 2.5c-.6 0-1 .5-1 1.2 0 2.7 2.5 5.3 5.3 5.3.7 0 1.2-.4 1.2-1L8 7l-1 .8C5.8 7.3 4.7 6.2 4.2 5L5 4z" fill="#121110"/></svg></li>
    <li>+ 542 581 7730<svg viewBox="0 0 12 12"><path d="M1 4.5C1 3 3 2 6 2s5 1 5 2.5V5H8.5V4h-5v1H1z"/><rect x="2" y="6" width="8" height="4.5" rx="1"/></svg></li>
    <li>info@ovekotiling.com<svg viewBox="0 0 12 12"><path d="M1 3h10v6.5H1z"/><path d="M1 3l5 3.6L11 3" fill="none" stroke="#121110" stroke-width="1"/></svg></li>
  </ul>
  <div class="address"><p>2180 Harbour View road</p><p>Washington, DC 20019</p></div>
</section>

<!-- Row 2 -->
<section class="card card--front card--dark" style="left:120px;top:357px;">
  <div class="tile-strip" role="img" aria-label="Dark diagonal floor-tile pattern"></div>
  <div class="front-name"><span class="word">Oveko</span><span class="sub">Tiling Services</span></div>
  <p class="web">www.ovekotiling.com</p>
</section>

<section class="card card--back" style="left:602px;top:357px;">
  <div class="tile-strip" role="img" aria-label="Light grey diagonal floor-tile pattern"></div>
  <div class="back-name"><span class="word">Oveko</span><span class="sub">Tiling Services</span></div>
  <div class="person"><p class="name">Daniel Harlow</p><p class="title">President</p></div>
  <ul class="contacts">
    <li>+ 254 5810 33470<svg viewBox="0 0 12 12"><rect x="0" y="0" width="12" height="12" rx="1.5"/><path d="M4 2.5c-.6 0-1 .5-1 1.2 0 2.7 2.5 5.3 5.3 5.3.7 0 1.2-.4 1.2-1L8 7l-1 .8C5.8 7.3 4.7 6.2 4.2 5L5 4z" fill="#fff"/></svg></li>
    <li>+ 542 581 7730<svg viewBox="0 0 12 12"><path d="M1 4.5C1 3 3 2 6 2s5 1 5 2.5V5H8.5V4h-5v1H1z"/><rect x="2" y="6" width="8" height="4.5" rx="1"/></svg></li>
    <li>info@ovekotiling.com<svg viewBox="0 0 12 12"><path d="M1 3h10v6.5H1z"/><path d="M1 3l5 3.6L11 3" fill="none" stroke="#fff" stroke-width="1"/></svg></li>
  </ul>
  <div class="address"><p>2180 Harbour View road</p><p>Washington, DC 20019</p></div>
</section>

<!-- Row 3 -->
<section class="card card--front" style="left:120px;top:689px;">
  <div class="tile-strip" role="img" aria-label="Light grey diagonal floor-tile pattern"></div>
  <div class="front-name"><span class="word">Oveko</span><span class="sub">Tiling Services</span></div>
  <p class="web">www.ovekotiling.com</p>
</section>

<section class="card card--back" style="left:602px;top:691px;">
  <div class="tile-strip" role="img" aria-label="Light grey diagonal floor-tile pattern"></div>
  <div class="back-name"><span class="word">Oveko</span><span class="sub">Tiling Services</span></div>
  <div class="person"><p class="name">Daniel Harlow</p><p class="title">President</p></div>
  <ul class="contacts">
    <li>+ 254 5810 33470<svg viewBox="0 0 12 12"><rect x="0" y="0" width="12" height="12" rx="1.5"/><path d="M4 2.5c-.6 0-1 .5-1 1.2 0 2.7 2.5 5.3 5.3 5.3.7 0 1.2-.4 1.2-1L8 7l-1 .8C5.8 7.3 4.7 6.2 4.2 5L5 4z" fill="#fff"/></svg></li>
    <li>+ 542 581 7730<svg viewBox="0 0 12 12"><path d="M1 4.5C1 3 3 2 6 2s5 1 5 2.5V5H8.5V4h-5v1H1z"/><rect x="2" y="6" width="8" height="4.5" rx="1"/></svg></li>
    <li>info@ovekotiling.com<svg viewBox="0 0 12 12"><path d="M1 3h10v6.5H1z"/><path d="M1 3l5 3.6L11 3" fill="none" stroke="#fff" stroke-width="1"/></svg></li>
  </ul>
  <div class="address"><p>2180 Harbour View road</p><p>Washington, DC 20019</p></div>
</section>

</body>
</html>
```